Change the world and help build JumpKOV.tv!

We need a mobile website design for our Beta release - see wireframes attached.
See our Logo design files attached along with fonts, etc.
Please see enclosed .PDF that provides a great overview of our company, KOV.
Any questions, feel free to ask - we're very engaged here on Pixel Harbor and will make ourselves available.
Thanks!
Tomas
Updates
Very pleased with what's coming in! Would like to see some more variety and more volume of designs.
Target Market(s)
Ages 13+ (all genders, races, creeds, income levels, etc)
Coding
Coded - Design and coding required
Number of Pages Required
5+ page
Font styles to use
Colors
Designer to choose colors to be used in the design.
Look and feel
Each slider illustrates characteristics of the customer's brand and the style your logo design should communicate.

```html
<!DOCTYPE html>
<html lang="en">
<head>
<meta charset="utf-8">
<title>JumpKOV.tv – Mobile Beta Screens</title>
<link rel="stylesheet" href="https://fonts.googleapis.com/css2?family=Bebas+Neue&family=Lato:wght@300;400;700&display=swap">
<style>
  :root {
    --page-bg: #eef0f7;
    --heading: #24345e;
    --screen-top: #34608f;
    --screen-mid: #26407a;
    --screen-bottom: #1b2856;
    --white: #ffffff;
    --soft-blue: #b7cbe6;
    --muted: #9fb0cf;
    --field-line: #7d93bb;
    --button-text: #1f2f5f;
    --video-black: #000000;
    --photo-light: #5a5a5a;
    --photo-dark: #111111;
    --like-red: #e0262b;
  }
  * { box-sizing: border-box; margin: 0; padding: 0; }
  html, body { width: 1200px; height: 2562px; overflow: hidden; }
  body {
    background: var(--page-bg);
    font-family: "Lato", sans-serif;
    color: var(--white);
    position: relative;
  }
  .screen-title {
    position: absolute;
    width: 400px;
    text-align: center;
    font: 400 16px "Lato", sans-serif;
    color: var(--heading);
    letter-spacing: 0.2px;
  }
  .screen {
    position: absolute;
    width: 323px;
    border-radius: 30px;
    overflow: hidden;
    background: linear-gradient(180deg, var(--screen-top) 0%, var(--screen-mid) 55%, var(--screen-bottom) 100%);
  }
  .screen.overflowing { border-radius: 30px 30px 0 0; }
  .status {
    position: absolute; top: 12px; left: 24px; right: 18px;
    display: flex; justify-content: space-between;
    font-size: 11px; color: var(--white);
  }
  .status-icons { display: flex; gap: 4px; align-items: center; }
  .brand {
    position: absolute; left: 12px; top: 80px;
    font: 700 19px/1 "Lato", sans-serif; color: var(--white);
  }
  .pill {
    position: absolute; right: 10px;
    border: 1px solid var(--soft-blue); border-radius: 16px;
    font: 400 13px/1 "Bebas Neue", sans-serif; letter-spacing: 0.4px;
    color: var(--white); padding: 8px 14px;
  }
  .pill.beta { top: 41px; }
  .pill.influencer { top: 83px; }
  .dark .pill { border-color: var(--white); }
  .video {
    position: absolute; left: 0; right: 0; top: 123px; height: 182px;
    background: var(--video-black);
  }
  .controls {
    position: absolute; left: 12px; right: 10px;
    display: flex; align-items: center; gap: 10px; font-size: 8px;
  }
  .progress { flex: 1; height: 2px; background: #8c8c8c; position: relative; }
  .progress::after {
    content: ""; position: absolute; left: 60%; top: -3px;
    width: 8px; height: 8px; border-radius: 50%; background: #bdbdbd;
  }
  .video-info { position: absolute; left: 10px; right: 12px; top: 325px; }
  .video-title { font: 700 18px "Lato", sans-serif; }
  .likes { margin: 10px 0 6px 2px; font-size: 14px; color: var(--muted); display: flex; align-items: center; gap: 6px; }
  .video-copy { font: 300 11.5px/22.5px "Lato", sans-serif; color: #d5deef; padding-left: 2px; }
  .cta {
    position: absolute; left: 12px; right: 12px; height: 45px;
    border-radius: 23px; background: var(--white);
    display: flex; align-items: center; justify-content: center;
    font: 400 19px/1 "Bebas Neue", sans-serif; color: var(--button-text); letter-spacing: 0.3px;
  }
  .footer-links {
    position: absolute; left: 0; right: 0;
    list-style: none; text-align: center;
    font: 300 9.5px/30px "Lato", sans-serif; color: var(--muted);
  }
  .photo {
    position: absolute; inset: 0;
    background: radial-gradient(ellipse at 55% 45%, var(--photo-light) 0%, #2c2c2c 50%, var(--photo-dark) 100%);
  }
  .back {
    position: absolute; left: 11px; top: 45px;
    border: 1px solid var(--soft-blue); border-radius: 13px;
    padding: 5px 9px; font-size: 8px; display: flex; align-items: center; gap: 3px;
  }
  .form-title {
    position: absolute; top: 40px; left: 0; right: 0; text-align: center;
    font: 400 30px/1 "Bebas Neue", sans-serif; letter-spacing: 0.2px;
  }
  .form-title.shifted { left: 82px; right: auto; }
  .intro {
    position: absolute; left: 11px; right: 14px; top: 88px;
    font: 700 12px/19px "Lato", sans-serif; color: var(--soft-blue);
  }
  .form { position: absolute; left: 6px; right: 10px; }
  .field {
    border: 1px solid var(--field-line); border-radius: 18px;
    height: 41px; padding: 0 22px; margin-bottom: 11px;
  }
  .field legend { font: 400 10px "Lato", sans-serif; color: var(--soft-blue); padding: 0 2px; }
  .field .value { font: 400 11px/14px "Lato", sans-serif; display: block; margin-top: 2px; }
  .field.story { height: 64px; border-radius: 26px; }
  .field.story .hint { display: block; margin-top: 34px; font-size: 7px; color: #51648f; }
  .thanks-title {
    position: absolute; top: 78px; left: 0; right: 0; text-align: center;
    font: 400 66px/1 "Bebas Neue", sans-serif;
  }
  .thanks-sub {
    position: absolute; top: 140px; left: 0; right: 0; text-align: center;
    font: 400 30px/1 "Bebas Neue", sans-serif;
  }
  .thanks-art {
    position: absolute; top: 190px; left: 50px; width: 223px; height: 150px;
    border-radius: 50%;
    background: radial-gradient(circle, #4a70a6 0%, #30528a 40%, rgba(48,82,138,0) 72%);
  }
  .thanks-copy {
    position: absolute; left: 18px; right: 18px; text-align: center;
    font: 400 11.5px/19px "Lato", sans-serif; color: var(--soft-blue);
  }
  .sign-love { position: absolute; left: 0; right: 0; text-align: center; font: 700 20px "Lato", sans-serif; }
  .sign-names { position: absolute; left: 0; right: 0; text-align: center; font-size: 12px; color: var(--soft-blue); }
  .back.centered { left: 50%; transform: translateX(-50%); }
</style>
</head>
<body>

<h2 class="screen-title" style="left:156px;top:28px;">HOME PAGE- OPTION 1</h2>
<h2 class="screen-title" style="left:656px;top:28px;">HOME PAGE- OPTION 2</h2>

<section class="screen home" style="left:207px;top:87px;height:703px;">
  <div class="status"><span>10:24</span><span class="status-icons">
    <svg width="12" height="8"><rect x="0" y="5" width="2" height="3" fill="#fff"/><rect x="3" y="3" width="2" height="5" fill="#fff"/><rect x="6" y="1" width="2" height="7" fill="#fff"/><rect x="9" y="0" width="2" height="8" fill="#fff"/></svg>
    <svg width="18" height="9"><rect x="0.5" y="0.5" width="15" height="8" rx="2" fill="none" stroke="#fff"/><rect x="2" y="2" width="12" height="5" fill="#fff"/></svg></span></div>
  <div class="brand">JumpKOV.tv</div>
  <span class="pill beta">JOIN BETA</span>
  <span class="pill influencer">INFLUENCER SIGN-UP</span>
  <div class="video"></div>
  <div class="controls" style="top:275px;">
    <svg width="22" height="22"><circle cx="11" cy="11" r="10" fill="none" stroke="#fff" stroke-width="1.5"/><rect x="8" y="7" width="2" height="8" fill="#fff"/><rect x="12" y="7" width="2" height="8" fill="#fff"/></svg>
    <div class="progress"></div><span>00:60</span>
    <svg width="10" height="10"><path d="M1 9 L9 1 M6 1 H9 V4 M1 6 V9 H4" stroke="#fff" fill="none"/></svg>
  </div>
  <div class="video-info">
    <h3 class="video-title">The Title of Video</h3>
    <p class="likes"><svg width="15" height="13"><path d="M7.5 13 L1.5 6.5 A3.5 3.5 0 0 1 7.5 2 A3.5 3.5 0 0 1 13.5 6.5 Z" fill="var(--like-red)"/></svg>1,234 Likes</p>
    <p class="video-copy">Lorem ipsum dolor sit amet, consectetur adipiscing elit. Cras accumsan ultrices ornare. Praesent in urna vel ligula malesuada lobortis. Aliquam id bibendum lorem. Donec consequat eu libero eu semper. Curabitur porttitor, sem ut fermentum varius, turpis nisi sollicitudin.</p>
  </div>
  <div class="cta" style="top:513px;">DONATE TO OUR FUNDHIVE CAMPAIGN!</div>
  <ul class="footer-links" style="top:570px;"><li>Terms and Conditions</li><li>Privacy Policy</li><li>About KOV The</li><li>KOV Team</li></ul>
</section>

<section class="screen home dark" style="left:700px;top:87px;height:703px;">
  <div class="photo" role="img" aria-label="Black and white close-up portrait photograph of a tearful person"></div>
  <div class="status"><span>10:24</span><span class="status-icons">
    <svg width="12" height="8"><rect x="0" y="5" width="2" height="3" fill="#fff"/><rect x="3" y="3" width="2" height="5" fill="#fff"/><rect x="6" y="1" width="2" height="7" fill="#fff"/><rect x="9" y="0" width="2" height="8" fill="#fff"/></svg>
    <svg width="18" height="9"><rect x="0.5" y="0.5" width="15" height="8" rx="2" fill="none" stroke="#fff"/><rect x="2" y="2" width="12" height="5" fill="#fff"/></svg></span></div>
  <div class="brand">JumpKOV.tv</div>
  <span class="pill beta">JOIN BETA</span>
  <span class="pill influencer">INFLUENCER SIGN-UP</span>
  <div class="controls" style="top:475px;">
    <svg width="22" height="22"><circle cx="11" cy="11" r="10" fill="none" stroke="#fff" stroke-width="1.5"/><rect x="8" y="7" width="2" height="8" fill="#fff"/><rect x="12" y="7" width="2" height="8" fill="#fff"/></svg>
    <div class="progress"></div><span>00:60</span>
    <svg width="10" height="10"><path d="M1 9 L9 1 M6 1 H9 V4 M1 6 V9 H4" stroke="#fff" fill="none"/></svg>
  </div>
  <div class="cta" style="top:513px;">DONATE TO OUR FUNDHIVE CAMPAIGN!</div>
  <ul class="footer-links" style="top:570px;"><li>Terms and Conditions</li><li>Privacy Policy</li><li>About KOV The</li><li>KOV Team</li></ul>
</section>

<h2 class="screen-title" style="left:156px;top:846px;">JOIN BETA</h2>
<h2 class="screen-title" style="left:662px;top:846px;">INFLUENCER SIGN-UP</h2>

<section class="screen overflowing" style="left:204px;top:905px;height:763px;">
  <div class="status"><span>10:24</span><span class="status-icons">
    <svg width="12" height="8"><rect x="0" y="5" width="2" height="3" fill="#fff"/><rect x="3" y="3" width="2" height="5" fill="#fff"/><rect x="6" y="1" width="2" height="7" fill="#fff"/><rect x="9" y="0" width="2" height="8" fill="#fff"/></svg>
    <svg width="18" height="9"><rect x="0.5" y="0.5" width="15" height="8" rx="2" fill="none" stroke="#fff"/><rect x="2" y="2" width="12" height="5" fill="#fff"/></svg></span></div>
  <span class="back"><svg width="6" height="8"><path d="M5 1 L1 4 L5 7" stroke="#fff" fill="none"/></svg>BACK</span>
  <h1 class="form-title shifted">INFLUENCER SIGN-UP</h1>
  <p class="intro">As a way of thanking you for joining the KOV Team, we're giving company stock and ongoing cash bonuses to the first 1,000 people to be accepted into the KOV Influencer Program.</p>
  <form class="form" style="top:170px;">
    <fieldset class="field"><legend>Name</legend><span class="value">John Smith</span></fieldset>
    <fieldset class="field"><legend>Date of birth</legend><span class="value">DD / MM / YYYY</span></fieldset>
    <fieldset class="field"><legend>Address</legend><span class="value">11/23 Lorem Ipsum, wreeyyur 34567868</span></fieldset>
    <fieldset class="field"><legend>Email</legend><span class="value">abcd@werrtyu.com</span></fieldset>
    <fieldset class="field"><legend>Mobile</legend><span class="value">1234567890</span></fieldset>
    <fieldset class="field"><legend>Link to your website</legend><span class="value">www.abcdefgh.com</span></fieldset>
    <fieldset class="field story"><legend>Share your story with us</legend><span class="hint">5000 Character Max</span></fieldset>
  </form>
  <div class="cta" style="top:568px;">REGISTER</div>
  <ul class="footer-links" style="top:626px;"><li>Terms and Conditions</li><li>Privacy Policy</li><li>About KOV The</li><li>KOV Team</li></ul>
</section>

<section class="screen" style="left:700px;top:905px;height:702px;">
  <div class="status"><span>10:24</span><span class="status-icons">
    <svg width="12" height="8"><rect x="0" y="5" width="2" height="3" fill="#fff"/><rect x="3" y="3" width="2" height="5" fill="#fff"/><rect x="6" y="1" width="2" height="7" fill="#fff"/><rect x="9" y="0" width="2" height="8" fill="#fff"/></svg>
    <svg width="18" height="9"><rect x="0.5" y="0.5" width="15" height="8" rx="2" fill="none" stroke="#fff"/><rect x="2" y="2" width="12" height="5" fill="#fff"/></svg></span></div>
  <span class="back"><svg width="6" height="8"><path d="M5 1 L1 4 L5 7" stroke="#fff" fill="none"/></svg>BACK</span>
  <h1 class="form-title">JOIN BETA</h1>
  <p class="intro">Sing-up to receive an invitation to join our pre-launch (Beta) version of KOV! Join our growing community of mental health warriors and help build a platform that can improve the lives of millions of people.</p>
  <form class="form" style="top:170px;">
    <fieldset class="field"><legend>Name</legend><span class="value">John Smith</span></fieldset>
    <fieldset class="field"><legend>Date of birth</legend><span class="value">DD / MM / YYYY</span></fieldset>
    <fieldset class="field"><legend>Address</legend><span class="value">11/23 Lorem Ipsum, wreeyyur 34567868</span></fieldset>
    <fieldset class="field"><legend>Email</legend><span class="value">abcd@werrtyu.com</span></fieldset>
    <fieldset class="field"><legend>Mobile</legend><span class="value">1234567890</span></fieldset>
    <fieldset class="field story"><legend>Share your story with us</legend><span class="hint">5000 Character Max</span></fieldset>
  </form>
  <div class="cta" style="top:512px;">REGISTER</div>
  <ul class="footer-links" style="top:570px;"><li>Terms and Conditions</li><li>Privacy Policy</li><li>About KOV The</li><li>KOV Team</li></ul>
</section>

<h2 class="screen-title" style="left:178px;top:1705px;">JOIN BETA- THANK YOU PAGE</h2>
<h2 class="screen-title" style="left:656px;top:1705px;">INFLUENCER SIGN-UP- THANK YOU PAGE</h2>

<section class="screen" style="left:213px;top:1765px;height:702px;">
  <div class="status"><span>10:24</span><span class="status-icons">
    <svg width="12" height="8"><rect x="0" y="5" width="2" height="3" fill="#fff"/><rect x="3" y="3" width="2" height="5" fill="#fff"/><rect x="6" y="1" width="2" height="7" fill="#fff"/><rect x="9" y="0" width="2" height="8" fill="#fff"/></svg>
    <svg width="18" height="9"><rect x="0.5" y="0.5" width="15" height="8" rx="2" fill="none" stroke="#fff"/><rect x="2" y="2" width="12" height="5" fill="#fff"/></svg></span></div>
  <h1 class="thanks-title">THANK YOU</h1>
  <p class="thanks-sub">FOR SIGNING UP!</p>
  <div class="thanks-art" role="img" aria-label="Illustration of praying hands in a circle surrounded by small stars"></div>
  <p class="thanks-copy" style="top:326px;">Please check your email for information about how our Beta program will work and what you can expect along the way.</p>
  <p class="thanks-copy" style="top:393px;left:12px;right:12px;">We're so excited to have you on the KOV Team! You're doing a wonderful thing for the world, and we are forever grateful for you!</p>
  <p class="sign-love" style="top:456px;">With Love,</p>
  <p class="sign-names" style="top:488px;">- Marla &amp; Tomas”</p>
  <span class="back centered" style="top:523px;"><svg width="6" height="8"><path d="M5 1 L1 4 L5 7" stroke="#fff" fill="none"/></svg>BACK</span>
  <ul class="footer-links" style="top:570px;"><li>Terms and Conditions</li><li>Privacy Policy</li><li>About KOV The</li><li>KOV Team</li></ul>
</section>

<section class="screen" style="left:700px;top:1765px;height:702px;">
  <div class="status"><span>10:24</span><span class="status-icons">
    <svg width="12" height="8"><rect x="0" y="5" width="2" height="3" fill="#fff"/><rect x="3" y="3" width="2" height="5" fill="#fff"/><rect x="6" y="1" width="2" height="7" fill="#fff"/><rect x="9" y="0" width="2" height="8" fill="#fff"/></svg>
    <svg width="18" height="9"><rect x="0.5" y="0.5" width="15" height="8" rx="2" fill="none" stroke="#fff"/><rect x="2" y="2" width="12" height="5" fill="#fff"/></svg></span></div>
  <h1 class="thanks-title">THANK YOU</h1>
  <p class="thanks-sub">FOR YOUR INTEREST!</p>
  <div class="thanks-art" role="img" aria-label="Illustration of praying hands in a circle surrounded by small stars"></div>
  <p class="thanks-copy" style="top:326px;">Please check your email for information about how KOV’s Influencer Program will work and what you can expect along the way.</p>
  <p class="thanks-copy" style="top:393px;left:12px;right:12px;">You’re doing a wonderful thing for the world, and we are forever grateful for you!</p>
  <p class="sign-love" style="top:436px;">With Love,</p>
  <p class="sign-names" style="top:468px;">- Marla &amp; Tomas”</p>
  <span class="back centered" style="top:523px;"><svg width="6" height="8"><path d="M5 1 L1 4 L5 7" stroke="#fff" fill="none"/></svg>BACK</span>
  <ul class="footer-links" style="top:570px;"><li>Terms and Conditions</li><li>Privacy Policy</li><li>About KOV The</li><li>KOV Team</li></ul>
</section>

</body>
</html>
```